Stationery Design Project for Marketing Consultancy

I have started a new consultancy business and require the following elements to be designed using existing logo:
• Business card
• Letterhead
• Envelope (DL, C4, C5)
• Microsoft word template for report writing
• A4 Presentation Folder
• Powerpoint template
COPY FOR FRONT AND BACK OF BUSINESS CARD
logo
'Countable Growth. Bold Outcomes' slogan (but no need to use existing lockup with logo)
name, B Bus. Mktg, Grad Dip Digital Mktg, CPM (post nominal abbreviations in smaller font)
mobile: 04XX-XXX-XXX (I will give details to the winner to add)
website: www.quorvale.com.au
email: info@quorvale.com.au
COPY FOR LETTERHEAD
Logo
Company Name
Please, submit your designs that include business card, letterhead and envelope. Once selected the winner will be asked to complete the project by creating the rest of the artwork.
FINAL FILES
Print ready files to be supplied as well as Indesign files so that minor amends can be made if necessary in future.
• Layered vectors in EPS & PDF
• Screen quality JPEG & PNGs
ABOUT THE BUSINESS: QUORVALE
I work with clients to understand their business challenges, developing and executing measurable marketing strategies tied to key business metrics. Services include:
Services include:
• Business planning and business development
• Marketing and brand strategy
• Insight-driven integrated campaigns
• Loyalty programs and retention marketing
• Marketing automation
• Direct marketing (traditional and digital)
• Content strategy and development
Hi everyone,
Target Market(s)
Corporate decision makers (heads of marketing, general managers etc) and small to medium sized business owners. Predominately male aged 35+
Industry/Entity Type
Marketing
Requirements
Must have
- BRAND PERSONALITY
The successful design will communicate brand personality. I am a professional, results-driven entrepreneur, but want to show off my creative flair.
MEMORABILITY
Looking for a unique and eye-catching design. Am considering special printing effects (die cuts, letterpress, interactive elements, embossing, foiling etc) or a striking minimalist approach.
Nice to have
- I have a mission that could be incorporated on reverse if room -
Turning insights into actions & passion into profit.
Should not have
- Use of pink or green.

```html
<!DOCTYPE html>
<html lang="en">
<head>
<meta charset="utf-8">
<title>Quorvale Stationery</title>
<link href="https://fonts.googleapis.com/css2?family=Montserrat:wght@400;600;700&display=swap" rel="stylesheet">
<style>
:root{
  --bg:#e8e5e1;
  --charcoal-top:#3a3a3a;
  --charcoal-bottom:#1c1c1c;
  --paper:#ffffff;
  --paper-shade:#ececec;
  --ink-light:#e6e6e6;
  --ink-muted:#9a9a9a;
  --ink-dark:#333333;
  --mark-faint:#e2e2e2;
}
*{margin:0;padding:0;box-sizing:border-box}
html,body{width:1200px;height:864px;overflow:hidden}
body{background:var(--bg);font-family:'Montserrat',sans-serif;position:relative}
.piece{position:absolute;box-shadow:0 4px 12px rgba(0,0,0,.25)}
.dark{background:linear-gradient(180deg,var(--charcoal-top),var(--charcoal-bottom))}

.brand{color:var(--ink-light);font-weight:700;letter-spacing:.06em;display:flex;align-items:center;gap:.4em}
.brand-dot{width:.7em;height:.7em;border-radius:50%;background:var(--ink-light)}
.tagline{color:var(--ink-muted);font-weight:600;text-transform:uppercase;letter-spacing:.04em}

/* C5 envelope */
.envelope-c5{left:214px;top:256px;width:296px;height:453px}
.envelope-c5 .flap{position:absolute;left:0;top:0;width:100%;height:84px;background:var(--paper);border-bottom:1px solid #d0d0d0}
.envelope-c5 .flap-tuck{position:absolute;top:60px;width:14px;height:26px;background:var(--charcoal-top)}
.envelope-c5 .flap-tuck.left{left:0;border-top-right-radius:14px}
.envelope-c5 .flap-tuck.right{right:0;border-top-left-radius:14px}
.envelope-c5 .lockup{position:absolute;left:0;right:0;top:240px;display:flex;flex-direction:column;align-items:center;gap:6px}
.envelope-c5 .brand{font-size:24px}
.envelope-c5 .tagline{font-size:6.5px}

/* DL envelope */
.envelope-dl{left:524px;top:170px;width:299px;height:152px}
.envelope-dl .brand{position:absolute;left:22px;bottom:18px;font-size:9px}
.contact{position:absolute;color:var(--ink-light);font-size:4.5px;line-height:1.6}
.contact strong{font-weight:700}
.envelope-dl .contact{left:165px;bottom:14px}
.envelope-dl .web{position:absolute;right:16px;bottom:16px;color:var(--ink-light);font-size:4.5px}

/* letterhead */
.letterhead{left:535px;top:343px;width:274px;height:364px;background:linear-gradient(180deg,var(--paper),var(--paper-shade))}
.letterhead .watermark{position:absolute;left:67px;top:90px;display:flex;align-items:center;gap:8px;color:var(--mark-faint);font-weight:700;font-size:22px;letter-spacing:.06em}
.letterhead .watermark .brand-dot{background:var(--mark-faint);width:18px;height:18px}
.letterhead .contact{left:16px;bottom:30px;color:var(--ink-dark)}
.letterhead .footer-band{position:absolute;left:0;right:0;bottom:0;height:14px;background:var(--charcoal-bottom)}
.letterhead .footer-band span{position:absolute;right:16px;top:4px;color:var(--ink-light);font-size:4.5px}

/* business cards */
.card{left:869px;width:135px;height:91px}
.card-front{top:342px}
.card-front .lockup{position:absolute;left:0;right:0;top:34px;display:flex;flex-direction:column;align-items:center;gap:4px}
.card-front .brand{font-size:13px}
.card-front .tagline{font-size:3.6px}
.card-back{top:446px;height:89px;width:133px}
.card-back .brand{position:absolute;right:8px;top:10px;font-size:6px}
.card-back .name{position:absolute;left:28px;top:28px;color:var(--ink-light);font-size:5.5px;font-weight:700}
.card-back .contact{left:28px;top:42px;font-size:4.5px}
</style>
</head>
<body>

<section class="piece dark envelope-c5" aria-label="C5 envelope">
  <div class="flap"></div>
  <div class="flap-tuck left"></div>
  <div class="flap-tuck right"></div>
  <div class="lockup">
    <div class="brand"><span class="brand-dot"></span>QUORVALE</div>
    <div class="tagline">Countable Growth. Bold Outcomes.</div>
  </div>
</section>

<section class="piece dark envelope-dl" aria-label="DL envelope">
  <div class="brand"><span class="brand-dot"></span>QUORVALE</div>
  <div class="contact"><strong>Company Name</strong><br>M 04XX XXX XXX<br>E info@quorvale.com.au</div>
  <div class="web">www.quorvale.com.au</div>
</section>

<section class="piece letterhead" aria-label="Letterhead">
  <div class="watermark"><span class="brand-dot"></span>QUORVALE</div>
  <div class="contact"><strong>Company Name</strong><br>M 04XX XXX XXX<br>E info@quorvale.com.au</div>
  <div class="footer-band"><span>www.quorvale.com.au</span></div>
</section>

<section class="piece dark card card-front" aria-label="Business card front">
  <div class="lockup">
    <div class="brand"><span class="brand-dot"></span>QUORVALE</div>
    <div class="tagline">Countable Growth. Bold Outcomes.</div>
  </div>
</section>

<section class="piece dark card card-back" aria-label="Business card back">
  <div class="brand">QUORVALE</div>
  <div class="name">Company Name</div>
  <div class="contact">M 04XX XXX XXX<br>E info@quorvale.com.au<br><strong>www.quorvale.com.au</strong></div>
</section>

</body>
</html>
```